Brindle Studios First Business Card

I'm a real estate photographer in Maryland who also does 3D scans, walk through videos and use a drone for pictures and video as well. I have my drone license to fly commercially. I need a business card for my small business. I was thinking of just the dark logo on one side and contact/business info on the other but open to other creative ideas.
Target Market(s)
Real estate agents in Maryland
Industry/Entity Type
Real Estate
Contact Information for Business Card
Name: Marcus Pellingham, Position: Photographer and Owner, Email: marcus@brindlestudios.example, Website: brindlestudios.example, Phone: 301-555-0148

```html
<!DOCTYPE html>
<html lang="en">
<head>
<meta charset="utf-8">
<title>Brindle Studios – Business Card</title>
<link rel="stylesheet" href="https://fonts.googleapis.com/css2?family=Montserrat:wght@300;400;500;700&display=swap">
<style>
  :root {
    --backdrop: #3b3b3d;
    --card-white: #ffffff;
    --card-black: #1f1f1f;
    --blush: #e6bfa6;
    --ink: #1c1c1c;
    --rule: #b9b9b9;
  }
  * { box-sizing: border-box; margin: 0; padding: 0; }
  html, body {
    width: 1200px; height: 1200px; overflow: hidden;
    background: var(--backdrop);
    font-family: "Montserrat", sans-serif;
  }
  .stage {
    width: 1200px; height: 1200px;
    display: flex; flex-direction: column; align-items: center; justify-content: center;
    gap: 60px;
  }
  .card {
    position: relative;
    width: 880px; height: 503px;
    border-radius: 40px;
    border: 3px solid var(--blush);
    box-shadow: 0 14px 34px rgba(0,0,0,.35);
    overflow: hidden;
  }
  .card--front { background: var(--card-white); }
  .card--back { background: var(--card-black); }

  .wordmark {
    position: absolute;
    color: var(--blush);
    font-weight: 300;
    letter-spacing: .06em;
    white-space: nowrap;
    text-transform: uppercase;
  }
  .card--front .wordmark {
    left: 0; right: 0; top: 120px; text-align: center;
    font-size: 46px;
  }
  .card--back .wordmark {
    left: 0; right: 0; top: 212px; text-align: center;
    font-size: 74px;
  }

  .identity {
    position: absolute; left: 84px; top: 362px;
    border-left: 6px solid var(--blush);
    padding-left: 14px;
  }
  .identity__name {
    color: var(--blush); font-weight: 700; font-size: 36px; line-height: 1;
    letter-spacing: .01em;
  }
  .identity__role {
    color: var(--ink); font-weight: 400; font-size: 22px; margin-top: 6px;
  }

  .divider {
    position: absolute; left: 510px; top: 250px;
    width: 1px; height: 190px; background: var(--rule);
  }

  .contacts {
    position: absolute; left: 548px; top: 262px;
    list-style: none;
    color: var(--ink); font-size: 19px; line-height: 1.2;
  }
  .contacts li { display: flex; align-items: flex-start; gap: 12px; margin-bottom: 10px; }
  .contacts svg { flex: 0 0 22px; width: 22px; height: 22px; margin-top: 1px; }
  .contacts .icon { fill: none; stroke: var(--blush); stroke-width: 2; }
  .contacts .icon--solid { fill: var(--blush); stroke: none; }
</style>
</head>
<body>
<main class="stage">
  <section class="card card--front" aria-label="Business card front">
    <div class="wordmark">Brindle Studios</div>

    <div class="identity">
      <div class="identity__name">FULL NAME</div>
      <div class="identity__role">POSITION</div>
    </div>

    <div class="divider"></div>

    <ul class="contacts">
      <li>
        <svg viewBox="0 0 24 24"><path class="icon--solid" d="M6.6 10.8a15 15 0 0 0 6.6 6.6l2.2-2.2c.3-.3.7-.4 1-.2 1.1.4 2.3.6 3.6.6.6 0 1 .4 1 1V20c0 .6-.4 1-1 1A17 17 0 0 1 3 4c0-.6.4-1 1-1h3.5c.6 0 1 .4 1 1 0 1.3.2 2.5.6 3.6.1.3 0 .7-.2 1z"/></svg>
        <span>(000) 000 0000</span>
      </li>
      <li>
        <svg viewBox="0 0 24 24"><rect class="icon" x="2.5" y="5" width="19" height="14" rx="1"/><path class="icon" d="M3 6l9 7 9-7"/></svg>
        <span>email@company.com</span>
      </li>
      <li>
        <svg viewBox="0 0 24 24"><circle class="icon" cx="12" cy="12" r="9.5"/><path class="icon" d="M2.5 12h19M12 2.5c3 3 3 16 0 19M12 2.5c-3 3-3 16 0 19M4.5 7h15M4.5 17h15"/></svg>
        <span>www.company.com</span>
      </li>
      <li>
        <svg viewBox="0 0 24 24"><path class="icon--solid" d="M12 2a7 7 0 0 0-7 7c0 5 7 13 7 13s7-8 7-13a7 7 0 0 0-7-7zm0 9.5A2.5 2.5 0 1 1 12 6.5a2.5 2.5 0 0 1 0 5z"/></svg>
        <span>123 Name Street, 000<br>Your City, 00000-000</span>
      </li>
    </ul>
  </section>

  <section class="card card--back" aria-label="Business card back">
    <div class="wordmark">Brindle Studios</div>
  </section>
</main>
</body>
</html>
```